Crest Slogan Copy and Design

Create a slogan for Crest Vanguard a boxing, kick boxing, gym fitness equipment and clothing brand. We would like different versions (in terms of fonts and colours) of some of the slogans in the attached word document.

Updates
12 May 2:19PM - We have refined the slogans to use and don''t want you to come up with new slogans. We would like some slogans from the word file and submit them in different colours and fonts.

Themes
Tough
Professional
Quality
Updates

Target Market(s)

Requirements
Must have
• Multiple versions of the slogan - in terms of font and colourĀ 

Nice to have
• A version where the font is bold and solid suitable for use with a logo like thisĀ

```html
<!DOCTYPE html>
<html lang="en">
<head>
<meta charset="utf-8">
<title>Crest Vanguard — Slogans</title>
<link rel="stylesheet" href="https://fonts.googleapis.com/css2?family=Russo+One&display=swap">
<style>
  :root {
    --ink: #000000;
    --orange: #ff7f00;
    --amber: #ff9a1f;
    --lime: #80ff00;
    --sky: #29ccff;
    --paper: #ffffff;
  }
  html, body {
    margin: 0;
    padding: 0;
    width: 1200px;
    height: 969px;
    overflow: hidden;
    background: var(--paper);
  }
  .slogan-sheet {
    display: block;
    width: 1200px;
    height: 969px;
  }
  .slogan {
    font-family: "Russo One", "Arial Black", sans-serif;
    font-size: 88px;
    text-transform: lowercase;
  }
  .ink { fill: var(--ink); }
  .orange { fill: var(--orange); }
  .amber { fill: var(--amber); }
  .lime { fill: var(--lime); }
  .sky { fill: var(--sky); }
</style>
</head>
<body>
<svg class="slogan-sheet" viewBox="0 0 1200 969" xmlns="http://www.w3.org/2000/svg" role="group" aria-label="Crest Vanguard slogans">
  <text class="slogan" x="0" y="72" textLength="730" lengthAdjust="spacingAndGlyphs"><tspan class="ink">vengeance is a </tspan><tspan class="orange">virtue</tspan></text>
  <text class="slogan orange" x="0" y="196" textLength="553" lengthAdjust="spacingAndGlyphs">total domination</text>
  <text class="slogan lime" x="0" y="320" textLength="612" lengthAdjust="spacingAndGlyphs">champions prevail</text>
  <text class="slogan sky" x="0" y="444" textLength="585" lengthAdjust="spacingAndGlyphs">never back down</text>
  <text class="slogan" x="0" y="568" textLength="1182" lengthAdjust="spacingAndGlyphs"><tspan class="ink">by </tspan><tspan class="amber">professionals</tspan><tspan class="ink"> for </tspan><tspan class="amber">professionals</tspan></text>
  <text class="slogan lime" x="0" y="692" textLength="364" lengthAdjust="spacingAndGlyphs">fight wear</text>
  <text class="slogan orange" x="0" y="816" textLength="863" lengthAdjust="spacingAndGlyphs">crest vanguard fighter</text>
  <text class="slogan ink" x="0" y="940" textLength="815" lengthAdjust="spacingAndGlyphs">by fighters for fighters</text>
</svg>
</body>
</html>
```